Bar and Grill needs specials signage

I have attached a file called "daily specials" I need it changed - so there is 1 sign/poster for each day/special
also attached other items to show some styling. I want the new posters chalkboard format, styled along the lines of the drink designs attached.
The designs should be scaleable, and editable, I will print locally

```html
<!DOCTYPE html>
<html lang="en">
<head>
<meta charset="utf-8">
<title>Daily Specials Signage</title>
<link href="https://fonts.googleapis.com/css2?family=Pinyon+Script&family=Cinzel:wght@500&family=Amatic+SC:wght@700&family=Oswald:wght@400;500;700&family=Roboto+Condensed:wght@500&display=swap" rel="stylesheet">
<style>
  :root {
    --backdrop: #5f5f5f;
    --board-dark: #1c1c1c;
    --board-mid: #2b2b2b;
    --chalk: #f1efe8;
    --chalk-soft: rgba(241, 239, 232, 0.7);
    --red: #d9474a;
    --green: #a3c57c;
  }
  * { box-sizing: border-box; margin: 0; padding: 0; }
  html, body { width: 1200px; height: 640px; overflow: hidden; }
  body { background: var(--backdrop); position: relative; }

  .poster {
    position: absolute; top: 91px; width: 355px; height: 459px;
    background: radial-gradient(ellipse at 40% 35%, var(--board-mid), var(--board-dark) 80%);
    box-shadow: 2px 3px 6px rgba(0, 0, 0, 0.35);
    color: var(--chalk); text-align: center;
  }
  .poster--wednesday { left: 183px; }
  .poster--thursday { left: 662px; }
  .poster p, .poster h2 { white-space: nowrap; }

  .poster__frame { position: absolute; inset: 0; }

  .header { position: absolute; left: 0; right: 0; top: 0; }
  .header__daily {
    position: absolute; left: 0; right: 0; top: 20px;
    font-family: "Pinyon Script", cursive; font-size: 40px; line-height: 1;
  }
  .header__specials {
    position: absolute; left: 0; right: 0; top: 72px;
    font-family: "Cinzel", serif; font-weight: 500; font-size: 28px; letter-spacing: 2px; line-height: 1;
  }
  .header__cutlery {
    position: absolute; left: 164px; top: 104px; width: 28px; height: 52px;
    background: rgba(241, 239, 232, 0.5); border-radius: 4px;
  }

  .day { position: absolute; left: 0; right: 0; line-height: 1; font-weight: normal; }
  .day--wednesday {
    top: 168px; font-family: "Oswald", sans-serif; font-weight: 700;
    font-size: 44px; letter-spacing: 2px; color: var(--red);
  }
  .day--thursday {
    top: 152px; font-family: "Oswald", sans-serif; font-weight: 400;
    font-size: 54px; letter-spacing: 7px; color: var(--green);
  }

  .special { position: absolute; left: 0; right: 0; line-height: 1; }
  .special__title--steak {
    top: 242px; font-family: "Amatic SC", sans-serif; font-weight: 700;
    font-size: 40px; letter-spacing: 3px;
  }
  .special__detail--steak {
    top: 278px; font-family: "Amatic SC", sans-serif; font-weight: 700;
    font-size: 31px; line-height: 32px; letter-spacing: 2px;
  }
  .special__title--pizza {
    top: 244px; font-family: "Oswald", sans-serif; font-weight: 500;
    font-size: 34px; letter-spacing: 3px; color: var(--red);
  }
  .special__detail--pizza {
    top: 296px; font-family: "Roboto Condensed", sans-serif; font-weight: 500;
    font-size: 21px; line-height: 27px;
  }

  .artwork { position: absolute; border-radius: 10px; }
  .artwork--steak {
    left: 60px; top: 352px; width: 236px; height: 84px;
    background: linear-gradient(90deg, rgba(241,239,232,0.22), rgba(217,71,74,0.4) 50%, rgba(241,239,232,0.22));
  }
  .artwork--pizza {
    left: 76px; top: 362px; width: 212px; height: 66px;
    background: linear-gradient(90deg, rgba(163,197,124,0.4), rgba(241,239,232,0.28) 50%, rgba(241,239,232,0.22));
  }
</style>
</head>
<body>

<article class="poster poster--wednesday">
  <svg class="poster__frame" viewBox="0 0 355 459" fill="none" stroke="var(--chalk-soft)" stroke-width="1.2">
    <path d="M20 30 H335 M20 30 V440 M335 30 V440 M20 440 H335"/>
    <path d="M28 42 Q28 26 44 26 M327 42 Q327 26 311 26 M28 428 Q28 444 44 444 M327 428 Q327 444 311 444"/>
    <path d="M80 100 Q177 66 275 100 L252 150 Q177 140 103 150 Z"/>
    <path d="M20 150 H335 M20 219 H335"/>
    <path d="M95 233 H260" stroke="var(--red)" stroke-width="4" stroke-dasharray="1 3"/>
    <path d="M115 146 H240" stroke="var(--red)" stroke-width="2" stroke-dasharray="1 3"/>
  </svg>
  <header class="header">
    <p class="header__daily">Daily</p>
    <p class="header__specials">SPECIALS</p>
    <div class="header__cutlery" role="img" aria-label="Chalk drawing of spoon, fork and knife"></div>
  </header>
  <h2 class="day day--wednesday">WEDNESDAY</h2>
  <p class="special special__title--steak">STEAK NIGHT</p>
  <p class="special special__detail--steak">HAND CUT STRIP STEAK,<br>- POTATO AND SALAD -</p>
  <div class="artwork artwork--steak" role="img" aria-label="Chalk drawing of salad bowl, grilled steak with crossed fork and tongs, and potato"></div>
</article>

<article class="poster poster--thursday">
  <svg class="poster__frame" viewBox="0 0 355 459" fill="none" stroke="var(--chalk-soft)" stroke-width="1.2">
    <path d="M20 30 H335 M20 30 V440 M335 30 V440 M20 440 H335"/>
    <path d="M28 42 Q28 26 44 26 M327 42 Q327 26 311 26 M28 428 Q28 444 44 444 M327 428 Q327 444 311 444"/>
    <path d="M80 100 Q177 66 275 100 L252 150 Q177 140 103 150 Z"/>
    <path d="M20 150 H335 M20 219 H335"/>
    <path d="M95 233 H260" stroke="var(--chalk)" stroke-width="4" stroke-dasharray="1 3"/>
    <path d="M115 146 H240" stroke="var(--green)" stroke-width="2" stroke-dasharray="1 3"/>
  </svg>
  <header class="header">
    <p class="header__daily">Daily</p>
    <p class="header__specials">SPECIALS</p>
    <div class="header__cutlery" role="img" aria-label="Chalk drawing of spoon, fork and knife"></div>
  </header>
  <h2 class="day day--thursday">THURSDAY</h2>
  <p class="special special__title--pizza">PIZZA AND WINGS</p>
  <p class="special special__detail--pizza">BUY ANY LARGE PIZZA AND<br>GET 10 BONELESS WINGS FREE</p>
  <div class="artwork artwork--pizza" role="img" aria-label="Chalk drawing of basil leaves, a sliced pizza and a garlic bulb"></div>
</article>

</body>
</html>
```